KORBALT

The business want a professional looking business card. We have a scetch we will add but want the extra upgrade, and would like more suggestions for variations of our business cards.

```html
<!DOCTYPE html>
<html lang="en">
<head>
<meta charset="utf-8">
<title>KORBALT – Business Card</title>
<link rel="stylesheet" href="https://fonts.googleapis.com/css2?family=Cinzel:wght@500&family=Source+Sans+3:wght@400;600;700&family=Montserrat:wght@500&display=swap">
<style>
  :root {
    --paper: #ffffff;
    --card: #030303;
    --gold: #ecd08e;
    --gold-soft: #d8b46a;
    --gold-deep: #a57c38;
    --gold-light: #f5e2a0;
    --ink: #111111;
    --band: linear-gradient(120deg, #c9a45a 0%, #f3dd98 28%, #a67d39 55%, #d6b56d 78%, #f6e4a4 100%);
  }
  * { margin: 0; padding: 0; box-sizing: border-box; }
  html, body {
    width: 1200px; height: 1200px; overflow: hidden;
    background: var(--paper);
  }
  .sheet { position: relative; width: 1200px; height: 1200px; }

  .card {
    position: absolute;
    left: 209px;
    width: 789px; height: 472px;
    background: var(--card);
    box-shadow: 4px 5px 6px rgba(0,0,0,0.28);
    overflow: hidden;
  }
  .card--front { top: 116px; }
  .card--back { top: 620px; }

  /* Front */
  .company-title {
    position: absolute; left: 52px; top: 50px;
    font-family: "Cinzel", serif; font-weight: 500;
    font-size: 37px; letter-spacing: 0.5px;
    color: var(--gold);
    white-space: nowrap;
  }
  .title-rule {
    position: absolute; left: 52px; top: 98px;
    width: 64px; height: 1.5px; background: var(--gold-soft);
  }
  .person { position: absolute; left: 52px; top: 198px; }
  .person__name {
    font-family: "Source Sans 3", sans-serif; font-weight: 700;
    font-size: 30px; line-height: 1; letter-spacing: 0.3px;
    color: var(--gold);
  }
  .person__role {
    margin-top: 8px;
    font-family: "Source Sans 3", sans-serif; font-weight: 400;
    font-size: 23px; line-height: 1;
    color: var(--gold-soft);
  }
  .contact-band {
    position: absolute; left: 0; top: 290px;
    width: 393px; height: 138px;
    background: var(--band);
    list-style: none;
    padding: 16px 0 0 50px;
  }
  .contact-band__item {
    display: flex; align-items: center;
    height: 37.5px;
    font-family: "Source Sans 3", sans-serif; font-weight: 400;
    font-size: 20.5px; color: var(--ink);
  }
  .contact-band__icon {
    width: 18px; height: 18px; margin-right: 15px; flex: none;
  }

  .brand-lockup {
    position: absolute; left: 440px; top: 230px;
    width: 300px; text-align: center;
  }
  .brand-lockup__dot {
    display: block; margin: 0 auto 22px;
    width: 70px; height: 70px; border-radius: 50%;
    border: 3px solid var(--gold);
  }
  .brand-lockup__name {
    font-family: "Cinzel", serif; font-weight: 500;
    font-size: 36px; line-height: 1; letter-spacing: 12px;
    padding-left: 12px;
    color: var(--gold);
  }
  .brand-lockup__since {
    margin-top: 14px;
    font-family: "Montserrat", sans-serif; font-weight: 500;
    font-size: 13px; letter-spacing: 5.5px; padding-left: 5.5px;
    color: var(--gold);
  }

  /* Back */
  .accent-bar {
    position: absolute; left: 268px;
    width: 253px; height: 12px;
    background: var(--band);
  }
  .accent-bar--top { top: 0; }
  .accent-bar--bottom { bottom: 0; }
  .back-mark {
    position: absolute; left: 0; right: 0; top: 183px;
    text-align: center;
  }
  .back-mark__name {
    font-family: "Cinzel", serif; font-weight: 500;
    font-size: 66px; line-height: 1; letter-spacing: 24px;
    padding-left: 24px;
    color: var(--gold);
  }
  .back-mark__since {
    margin-top: 22px;
    font-family: "Montserrat", sans-serif; font-weight: 500;
    font-size: 24px; letter-spacing: 11px; padding-left: 11px;
    color: var(--gold);
  }
</style>
</head>
<body>
<main class="sheet">
  <section class="card card--front" aria-label="Business card front">
    <h1 class="company-title">KORBALT HAVSTAD</h1>
    <div class="title-rule"></div>

    <div class="person">
      <p class="person__name">LARS ERIK HAVSTAD</p>
      <p class="person__role">CEO &amp; Founder</p>
    </div>

    <ul class="contact-band">
      <li class="contact-band__item">
        <svg class="contact-band__icon" viewBox="0 0 18 18" aria-hidden="true">
          <rect x="4.5" y="0.8" width="9" height="16.4" rx="1.5" fill="none" stroke="#111" stroke-width="1.6"/>
          <line x1="7.5" y1="2.8" x2="10.5" y2="2.8" stroke="#111" stroke-width="1"/>
          <circle cx="9" cy="14.6" r="0.9" fill="#111"/>
        </svg>
        00 470 555 0142
      </li>
      <li class="contact-band__item">
        <svg class="contact-band__icon" viewBox="0 0 18 18" aria-hidden="true">
          <rect x="1" y="4" width="16" height="11" fill="#111"/>
          <polyline points="1.5,4.6 9,10.5 16.5,4.6" fill="none" stroke="#d6b56d" stroke-width="1.2"/>
          <line x1="1.5" y1="14.4" x2="7" y2="9.4" stroke="#d6b56d" stroke-width="1"/>
          <line x1="16.5" y1="14.4" x2="11" y2="9.4" stroke="#d6b56d" stroke-width="1"/>
        </svg>
        korbalt.llc@mailbox.com
      </li>
      <li class="contact-band__item">
        <svg class="contact-band__icon" viewBox="0 0 18 18" aria-hidden="true">
          <g fill="none" stroke="#111" stroke-width="1.2">
            <circle cx="9" cy="9" r="7.6"/>
            <ellipse cx="9" cy="9" rx="3.4" ry="7.6"/>
            <line x1="9" y1="1.4" x2="9" y2="16.6"/>
            <line x1="1.4" y1="9" x2="16.6" y2="9"/>
            <path d="M2.6 5.2 H15.4 M2.6 12.8 H15.4"/>
          </g>
        </svg>
        www.korbalt.llc
      </li>
    </ul>

    <div class="brand-lockup">
      <span class="brand-lockup__dot" aria-hidden="true"></span>
      <p class="brand-lockup__name">KORBALT</p>
      <p class="brand-lockup__since">SINCE 2026</p>
    </div>
  </section>

  <section class="card card--back" aria-label="Business card back">
    <div class="accent-bar accent-bar--top"></div>
    <div class="back-mark">
      <p class="back-mark__name">KORBALT</p>
      <p class="back-mark__since">SINCE 2026</p>
    </div>
    <div class="accent-bar accent-bar--bottom"></div>
  </section>
</main>
</body>
</html>
```